Brochure Design Project - Innovative Service for Pharma Industry

Our start up is based in Germany, near Munich and we provide an innovative Service for the pharma industry. We develop product trainings and general trainings online. The adressed audience for these trainings are pharmacies and medics. The parma industry could increase the number of trainings, while saving money (incl a success guarantee). Our (not yet finnished) corporate page can be reviewed here: www.brevoloq.biz, our 'product & service' page is www.kestrumlearn.com. The color code should be leaned towards the corporate page.

The brochure should be send to decision makers in the pharma industry and rise the interest in innovative service. Seriousity should meet modern & clear design.Something eye cathing on the front page might be required.

Target Market(s)

Usually more conservative decision makers within the pharma industry

Industry/Entity Type

Industry

Requirements
Must have
• Conceptional design for an brochure (Din A4 size) of approx 6-8 pages, that capture the key messages (exact content would be filled / provided from us)
Nice to have
• Implementing some of the pics / phrases on the home page www.brevolq.biz could be maybe nice. How about a personal statement from the founder combined with a pic(pic attached)? Both is no must....

```html
<!DOCTYPE html>
<html lang="en">
<head>
<meta charset="utf-8">
<title>Brevoloq – Brochure Spread</title>
<link href="https://fonts.googleapis.com/css2?family=Alegreya+SC:wght@400&family=Arimo:wght@400;700&family=Didact+Gothic&family=Jost:wght@500;600&family=Source+Sans+3:ital,wght@0,300;0,400;1,400&display=swap" rel="stylesheet">
<style>
  :root {
    --orange: #f05a1e;
    --orange-soft: #f5a37e;
    --ink: #4a4a4a;
    --ink-soft: #6b6b6b;
    --dark-band: #3a3a3a;
    --paper: #ffffff;
    --backdrop: #d9d9d9;
    --photo-warm: #e9e2da;
  }
  * { box-sizing: border-box; margin: 0; padding: 0; }
  html, body { width: 1200px; height: 866px; overflow: hidden; }
  body { background: var(--backdrop); position: relative; font-family: "Didact Gothic", sans-serif; color: var(--ink); }

  .spread { position: absolute; left: 20px; top: 22px; width: 1160px; height: 822px; background: var(--paper); display: flex; box-shadow: 0 2px 8px rgba(0,0,0,.18); }
  .page { position: relative; width: 580px; height: 822px; overflow: hidden; }
  .page--back { border-right: 1px solid #d4d4d4; }

  .page svg.deco { position: absolute; left: 0; top: 0; }

  /* back page */
  .quote { position: absolute; left: 27px; top: 52px; width: 320px; font-family: "Alegreya SC", serif; font-size: 9.5px; letter-spacing: .6px; color: #222; line-height: 12px; }
  .quote span { display: block; }
  .quote .line-2 { padding-left: 90px; }
  .quote .author { position: absolute; right: -2px; bottom: 0; font-style: italic; }

  .hero-photo { position: absolute; left: 13px; top: 77px; width: 335px; height: 192px; background: linear-gradient(100deg, #2a2a2a 0%, #6e6e6e 40%, #b9c6c2 60%, #e4e4e4 100%); }
  .page-edge { position: absolute; left: 0; top: 77px; width: 13px; height: 192px; background: #9a9a9a; }

  .value-claim { position: absolute; left: 370px; top: 94px; width: 190px; font-family: "Source Sans 3", sans-serif; font-weight: 300; font-size: 13.4px; line-height: 16.6px; color: var(--orange); }

  .definition { position: absolute; left: 42px; top: 352px; width: 500px; font-family: "Jost", sans-serif; font-weight: 600; font-size: 11px; line-height: 14px; color: var(--orange); }
  .source { position: absolute; right: 45px; top: 387px; font-size: 8px; color: var(--ink-soft); }

  .founder-photo { position: absolute; left: 42px; top: 420px; width: 157px; height: 125px; border: 3px solid var(--orange); border-radius: 8px; background: linear-gradient(90deg, #d8d8d8, #a9a49e 55%, #ececec); }

  .company-story { position: absolute; left: 224px; top: 418px; width: 315px; font-size: 10.4px; line-height: 13.4px; color: var(--ink); }
  .company-story p + p { margin-top: 13px; }

  .imprint-mark { position: absolute; left: 45px; top: 700px; display: flex; align-items: center; gap: 5px; font-family: "Didact Gothic", sans-serif; font-size: 17px; color: var(--orange); }
  .imprint-mark .dot { width: 9px; height: 9px; border-radius: 50%; background: var(--orange); }

  .imprint { position: absolute; left: 161px; top: 678px; font-family: "Arimo", sans-serif; font-size: 10.8px; line-height: 17.5px; color: var(--ink); }
  .imprint .firm { color: var(--orange); font-weight: 700; }
  .imprint .sep { color: var(--orange); padding: 0 5px; }
  .imprint .gap { margin-top: 10px; }

  .web { position: absolute; right: 23px; top: 788px; font-family: "Arimo", sans-serif; font-size: 12px; color: var(--orange); }

  /* front page */
  .brand { position: absolute; left: 24px; top: 158px; width: 200px; text-align: center; }
  .brand .dot { display: block; width: 14px; height: 14px; border-radius: 50%; background: var(--orange); margin: 0 auto 10px; }
  .brand .name { display: block; font-family: "Didact Gothic", sans-serif; font-size: 40px; line-height: 1; color: var(--orange); letter-spacing: 1px; }
  .brand .tag { display: block; margin-top: 4px; font-family: "Arimo", sans-serif; font-weight: 700; font-size: 11px; color: var(--ink-soft); letter-spacing: .3px; }

  .promise { position: absolute; left: 272px; top: 98px; width: 272px; text-align: center; font-family: "Source Sans 3", sans-serif; font-weight: 300; font-size: 19.5px; line-height: 23px; color: var(--ink-soft); }
  .promise p + p { margin-top: 24px; }

  .tagline { position: absolute; left: 29px; top: 726px; font-family: "Source Sans 3", sans-serif; font-style: italic; font-size: 19px; color: var(--ink); }
</style>
</head>
<body>
<main class="spread">

  <section class="page page--back">
    <svg class="deco" width="580" height="822" viewBox="0 0 580 822" aria-hidden="true">
      <defs>
        <linearGradient id="top-swoosh" x1="0" x2="1">
          <stop offset="0" stop-color="#f05a1e"/>
          <stop offset=".6" stop-color="#f28a5c"/>
          <stop offset="1" stop-color="#f05a1e" stop-opacity="0"/>
        </linearGradient>
        <linearGradient id="grey-swoosh" x1="0" x2="1">
          <stop offset="0" stop-color="#3a3a3a"/>
          <stop offset=".7" stop-color="#8c8c8c"/>
          <stop offset="1" stop-color="#cfcfcf" stop-opacity="0"/>
        </linearGradient>
      </defs>
      <path d="M0,0 H290 Q440,18 528,68 Q360,34 0,40 Z" fill="url(#top-swoosh)"/>
      <path d="M0,272 Q210,262 425,262 Q230,272 0,300 Z" fill="url(#grey-swoosh)"/>
    </svg>

    <blockquote class="quote">
      <span>„ I wonder why people are afraid of new ideas.</span>
      <span class="line-2">I'm afraid of the old ones.“</span>
      <cite class="author">Jonas Kerr</cite>
    </blockquote>

    <div class="page-edge"></div>
    <div class="hero-photo" role="img" aria-label="Close-up photo of a woman wearing glasses, a screen reflected in the lens"></div>

    <p class="value-claim">We believe that products and services must offer added value for customers in order to generate them success. Get an overview of our benefits which you can find on this scale only with us.</p>

    <p class="definition">* Additive (Latin additivum added, enclosed), and adjuvant or additive … the products will be added in small amounts to achieve or improve certain properties.</p>
    <p class="source">* SOURCE: OPEN LEXICON</p>

    <div class="founder-photo" role="img" aria-label="Portrait photo of the company founder in a dark suit"></div>

    <div class="company-story">
      <p>The company was founded in 2011 in Munich by taking advantage of the newest technologies to offer advanced CLOUD E-LEARNING solutions.</p>
      <p>Here we aim at vertical markets of complex products. Together with our customers to develop newest concepts and operate platforms to cover their individual needs is our job.</p>
      <p>The successful initial implementation of an industrial expanses e-Learning Platform serves as the foundation to expand the service to other countries or target groups.</p>
      <p>The pharmaceutical industry is the primary target market for our company.</p>
    </div>

    <div class="imprint-mark"><span class="dot"></span>brevoloq</div>

    <address class="imprint">
      <div class="firm">brevoloq e.K.</div>
      <div>Lindenallee 42<span class="sep">|</span>82140 Olching (bei München)</div>
      <div>Tel +49 89 000 118 40<span class="sep">|</span>Fax +49 89 000 118 42</div>
      <div class="gap">HRA 10482<span class="sep">|</span>Amtsgericht Musterstadt</div>
      <div>FA Musterstadt<span class="sep">|</span>USt-IdNr.: DE100200300</div>
      <div>Geschäftsführer: M. Halvorsen</div>
    </address>

    <div class="web">www.brevoloq.biz</div>
  </section>

  <section class="page page--front">
    <svg class="deco" width="580" height="822" viewBox="0 0 580 822">
      <defs>
        <linearGradient id="photo-tone" x1="0" y1="0" x2="1" y2="1">
          <stop offset="0" stop-color="#efe7df"/>
          <stop offset=".45" stop-color="#d9c3b3"/>
          <stop offset=".8" stop-color="#e6e9ec"/>
          <stop offset="1" stop-color="#f4f4f4"/>
        </linearGradient>
        <linearGradient id="band-dark" x1="0" x2="1">
          <stop offset="0" stop-color="#2e2e2e"/>
          <stop offset=".7" stop-color="#777"/>
          <stop offset="1" stop-color="#bbb" stop-opacity="0"/>
        </linearGradient>
        <linearGradient id="band-orange" x1="0" x2="1">
          <stop offset="0" stop-color="#f05a1e"/>
          <stop offset=".75" stop-color="#f3875a"/>
          <stop offset="1" stop-color="#f5a37e" stop-opacity="0"/>
        </linearGradient>
        <linearGradient id="band-orange-rev" x1="1" x2="0">
          <stop offset="0" stop-color="#f05a1e"/>
          <stop offset=".7" stop-color="#f3875a"/>
          <stop offset="1" stop-color="#f5a37e" stop-opacity="0"/>
        </linearGradient>
        <linearGradient id="band-dark-rev" x1="1" x2="0">
          <stop offset="0" stop-color="#2e2e2e"/>
          <stop offset=".65" stop-color="#888"/>
          <stop offset="1" stop-color="#ccc" stop-opacity="0"/>
        </linearGradient>
      </defs>
      <path role="img" aria-label="Photo of a smiling team of young professionals seated at a table with a laptop"
            d="M0,346 Q260,286 580,279 V620 Q330,650 0,677 Z" fill="url(#photo-tone)"/>
      <path d="M0,300 Q180,262 360,257 Q170,276 0,322 Z" fill="url(#band-dark)"/>
      <path d="M0,336 Q220,278 430,270 Q200,300 0,370 Z" fill="url(#band-orange)"/>
      <path d="M380,705 Q480,680 580,620 V650 Q490,692 380,705 Z" fill="url(#band-orange-rev)"/>
      <path d="M250,735 Q430,712 580,660 V690 Q440,728 250,735 Z" fill="url(#band-dark-rev)"/>
    </svg>

    <div class="brand">
      <span class="dot"></span>
      <span class="name">brevoloq</span>
      <span class="tag">THE E-LEARNING COMPANY</span>
    </div>

    <div class="promise">
      <p>We provide an innovative Service for the pharma industry.</p>
      <p>We develop product trainings and general trainings online</p>
    </div>

    <p class="tagline">No Limits - Going Beyond Borders</p>

    <div class="web">www.brevoloq.biz</div>
  </section>

</main>
</body>
</html>
```